International Wholesale Food Company Needs Packaging Design for new products

We have a logo for our new business. It is attached. Now we need a packaging design for some new products that we will be selling. These items will be packaged in clear plastic bags. We are an international wholesale foods company selling foods imported from West Africa. We are just in the process of launching. We're looking for a design that is fresh and modern.

These items below are what we need packaging design for:

Cassava Leaves-500 g- Clear Plastic Bag
Sweet potato leaves-500 g-Clear Plastic Bag

```html
<!DOCTYPE html>
<html lang="en">
<head>
<meta charset="utf-8">
<title>Savanna Pantry – Sweet Potato Leaves Label</title>
<link rel="stylesheet" href="https://fonts.googleapis.com/css2?family=Cinzel:wght@400;500&family=Montserrat:wght@400;500;600&display=swap">
<style>
  :root {
    --canvas-bg: #f2f2f2;
    --label-white: #ffffff;
    --pattern-grey: #ececec;
    --brand-red: #c4212b;
    --leaf-green: #1f6b3a;
    --leaf-light: #4f8f3c;
    --ink: #333333;
  }
  * { margin: 0; padding: 0; box-sizing: border-box; }
  html, body {
    width: 1200px;
    height: 1200px;
    overflow: hidden;
    background: var(--canvas-bg);
  }
  .canvas {
    position: relative;
    width: 1200px;
    height: 1200px;
  }
  .label {
    position: absolute;
    left: 280px;
    top: 130px;
    width: 640px;
    height: 940px;
  }
  .label-shape {
    position: absolute;
    inset: 0;
    width: 640px;
    height: 940px;
  }
  .brand-mark {
    position: absolute;
    left: 50%;
    top: 40px;
    width: 124px;
    height: 124px;
    margin-left: -62px;
    border-radius: 50%;
    border: 3px solid var(--brand-red);
    background: var(--label-white);
  }
  .brand-name {
    position: absolute;
    top: 180px;
    width: 100%;
    text-align: center;
    font-family: "Montserrat", sans-serif;
    font-weight: 500;
    font-size: 30px;
    letter-spacing: 0.5px;
    color: var(--brand-red);
  }
  .product-line {
    position: absolute;
    top: 258px;
    width: 100%;
    text-align: center;
    font-family: "Cinzel", serif;
    font-size: 46px;
    color: var(--brand-red);
  }
  .product-name {
    position: absolute;
    top: 308px;
    width: 100%;
    text-align: center;
    font-family: "Cinzel", serif;
    font-weight: 500;
    font-size: 104px;
    line-height: 1;
    color: var(--leaf-green);
  }
  .product-local {
    position: absolute;
    top: 428px;
    width: 100%;
    text-align: center;
    font-family: "Cinzel", serif;
    font-size: 17px;
    letter-spacing: 4px;
    color: var(--ink);
  }
  .product-photo {
    position: absolute;
    left: 90px;
    top: 470px;
    width: 460px;
    height: 270px;
    border-radius: 50% 50% 40% 40%;
    background: radial-gradient(ellipse at center, var(--leaf-light) 0%, var(--leaf-green) 60%, rgba(31,107,58,0) 72%);
  }
  .net-weight {
    position: absolute;
    left: 60px;
    top: 780px;
    font-family: "Montserrat", sans-serif;
    font-size: 20px;
    line-height: 1.35;
    color: var(--ink);
  }
  .natural-badge {
    position: absolute;
    right: 60px;
    top: 760px;
    width: 90px;
    height: 90px;
    border-radius: 50%;
    border: 3px solid var(--leaf-light);
    background: var(--label-white);
  }
</style>
</head>
<body>
<main class="canvas">
  <section class="label">
    <svg class="label-shape" viewBox="0 0 640 940" aria-hidden="true">
      <defs>
        <radialGradient id="labelPatternTone" cx="50%" cy="55%" r="65%">
          <stop offset="0%" stop-color="#f4f4f4"/>
          <stop offset="100%" stop-color="#ffffff"/>
        </radialGradient>
      </defs>
      <path d="M20 140 Q20 110 50 110 L150 110 L150 30 Q150 0 180 0 L460 0 Q490 0 490 30 L490 110 L590 110 Q620 110 620 140 L620 900 Q620 930 590 930 L50 930 Q20 930 20 900 Z"
            fill="url(#labelPatternTone)" role="img" aria-label="Faint circular decorative pattern on white label background"/>
      <path d="M24 150 L24 142 Q24 114 52 114 L154 114 L154 32 Q154 4 182 4 L458 4 Q486 4 486 32 L486 114 L588 114 Q616 114 616 142 L616 150"
            fill="none" stroke="var(--brand-red)" stroke-width="8"/>
    </svg>

    <div class="brand-mark" aria-hidden="true"></div>
    <div class="brand-name">SAVANNA PANTRY</div>

    <h1 class="product-line">SWEET POTATO</h1>
    <div class="product-name">LEAVES</div>
    <div class="product-local">(METAMBELE)</div>

    <div class="product-photo" role="img" aria-label="Photo of a fresh bunch of green sweet potato leaves"></div>

    <p class="net-weight">Net Wt.<br>500 g</p>
    <div class="natural-badge" aria-hidden="true"></div>
  </section>
</main>
</body>
</html>
```